Billboard design - consider what a billboard is

Design a billboard using my logo - Billboard is 6m x 3m
A Billboard is advertising for my company that is on a big sign.

Has to be clean and easy to read, and ideally highlights that we are Residential and Commercial builders.

Keep it clean and easy to read

The contact number for the board is

022 583 7092
www.harbourframeworks.co.nz
info@harbourframeworks.co.nz

Doesnt have to have all contact details if it doesnt fit

Has to catch peoples attention to contact us if they need a builder

Can you please change the sign to be all white writing, with black background ?
Updates

Please consider what a billboard is...

The design needs to be suitable for a billboard..

Target Market(s)

people driving past

Industry/Entity Type

Construction

Logo Text

Wellington Builder, website email address, contact number

Colors
0054AA
0677BA
7BADD7
CADEEF
E8F1F8

Requirements
Must have
• Easy to read
Nice to have
• easy to read, can clearly see contact details

```html
<!DOCTYPE html>
<html lang="en">
<head>
<meta charset="utf-8">
<title>Wellington Builder Billboard – Harbour Frameworks</title>
<link rel="stylesheet" href="https://fonts.googleapis.com/css2?family=Orbitron:wght@500;700;800;900&family=Montserrat:wght@400&display=swap">
<style>
  :root {
    --ink-dark: #0b0b0c;
    --ink-mid: #18191b;
    --text-white: #ffffff;
    --brand-blue: #5f8dc5;
  }
  html, body {
    margin: 0;
    padding: 0;
    width: 1200px;
    height: 600px;
    overflow: hidden;
    background: var(--ink-dark);
  }
  .billboard {
    display: block;
    width: 1200px;
    height: 600px;
  }
  .headline-city {
    font-family: "Orbitron", sans-serif;
    font-weight: 800;
    font-size: 79px;
    fill: var(--text-white);
  }
  .headline-trade {
    font-family: "Orbitron", sans-serif;
    font-weight: 900;
    font-size: 194px;
    fill: var(--brand-blue);
  }
  .tagline {
    font-family: "Orbitron", sans-serif;
    font-weight: 500;
    font-size: 40px;
    fill: var(--text-white);
  }
  .brand-name {
    font-family: "Orbitron", sans-serif;
    font-weight: 800;
    font-size: 30px;
    fill: var(--brand-blue);
  }
  .phone-number {
    font-family: "Orbitron", sans-serif;
    font-weight: 500;
    font-size: 52px;
    fill: var(--text-white);
  }
  .contact-line {
    font-family: "Montserrat", sans-serif;
    font-weight: 400;
    font-size: 20px;
    fill: var(--text-white);
  }
  .icon-stroke {
    fill: none;
    stroke: var(--brand-blue);
    stroke-linecap: round;
    stroke-linejoin: round;
  }
</style>
</head>
<body>
<svg class="billboard" viewBox="0 0 1200 600" xmlns="http://www.w3.org/2000/svg">
  <defs>
    <linearGradient id="site-tone" x1="0" y1="0" x2="1" y2="1">
      <stop offset="0" stop-color="#0a0a0b"/>
      <stop offset="0.55" stop-color="#151618"/>
      <stop offset="1" stop-color="#0c0c0d"/>
    </linearGradient>
  </defs>

  <rect class="backdrop-photo" role="img" aria-label="Darkened aerial photo of a construction site" x="0" y="0" width="1200" height="600" fill="url(#site-tone)"/>

  <text class="headline-city" x="272" y="136" textLength="657" lengthAdjust="spacingAndGlyphs">WELLINGTON</text>
  <text class="headline-trade" x="81" y="310" textLength="1038" lengthAdjust="spacingAndGlyphs">BUILDER</text>
  <text class="tagline" x="269" y="369" textLength="660" lengthAdjust="spacingAndGlyphs">Residential and Commercial</text>

  <g class="brand">
    <text class="brand-name" x="81" y="470" textLength="233" lengthAdjust="spacingAndGlyphs">HARBOUR</text>
    <text class="brand-name" x="81" y="512" textLength="233" lengthAdjust="spacingAndGlyphs">FRAMEWORKS</text>
  </g>

  <g class="phone-icon icon-stroke" stroke-width="3.5" transform="translate(582 438)">
    <path d="M8 2 C2 4 0 10 2 18 C6 32 20 46 36 51 C44 53 50 51 52 45 L52 40 C52 38 51 37 49 36 L40 32 C38 31 36 32 35 33 L32 37 C24 33 19 28 15 20 L19 17 C21 16 21 14 20 12 L16 3 C15 1 13 1 11 1 Z"/>
  </g>
  <text class="phone-number" x="659" y="484" textLength="459" lengthAdjust="spacingAndGlyphs">022 583 7092</text>

  <g class="mail-icon icon-stroke" stroke-width="1.8" transform="translate(369 507)">
    <rect x="0.5" y="0.5" width="14" height="10" rx="1.5"/>
    <path d="M1 1.5 L7.5 6.5 L14 1.5"/>
  </g>
  <text class="contact-line" x="389" y="519">info@harbourframeworks.co.nz</text>

  <g class="web-icon icon-stroke" stroke-width="1.5" transform="translate(763 512)">
    <circle cx="0" cy="0" r="7.5"/>
    <ellipse cx="0" cy="0" rx="3.2" ry="7.5"/>
    <path d="M-7.5 0 H7.5 M-6.5 -3.8 H6.5 M-6.5 3.8 H6.5"/>
  </g>
  <text class="contact-line" x="1119" y="519" text-anchor="end">www.harbourframeworks.co.nz</text>
</svg>
</body>
</html>
```